ParcelLantern shopping service flyer

We are a Korean shopping service. The attached picture explains our service. We would like to create a postcard or slightly larger sized flyer advertising our service. Front side will be graphics and back side text. For the front side, we want an updated version of the attached picture with our new logo and colours. And for the back side, create a simple design on the back side which we can enter all the text. Need font and design options.

Target Market(s)

20s and 30s females shopping for clothing (people not in Korea), shoppers are not Korean.

Industry/Entity Type

Online Shopping

Requirements
Must have
• For the front side, we want an updated version of the attached picture with our new logo and colours. And for the back side, create a simple design on the back side which we can enter all the text. Need font and design options.
Nice to have
• Little to no text on the front side.

```html
<!DOCTYPE html>
<html lang="en">
<head>
<meta charset="utf-8">
<title>ParcelLantern shopping service flyer</title>
<link href="https://fonts.googleapis.com/css2?family=Bebas+Neue&family=Open+Sans:ital,wght@0,400;0,600;0,700;1,600&display=swap" rel="stylesheet">
<style>
  :root {
    --teal: #1f9e8c;
    --teal-soft: #55bfae;
    --teal-deep: #1a8f7f;
    --teal-ring: #4bb8a8;
    --coral: #ec7a4e;
    --paper: #f4f4f4;
    --paper-grey: #e6e7e7;
    --ink: #1b1b1b;
    --white: #ffffff;
    --backdrop: #d9dadb;
  }
  * { box-sizing: border-box; margin: 0; padding: 0; }
  html, body { width: 966px; height: 1200px; overflow: hidden; }
  body {
    background: var(--backdrop);
    font-family: "Open Sans", Arial, sans-serif;
    color: var(--ink);
    position: relative;
  }
  .card {
    position: absolute;
    left: 178px;
    width: 610px;
    height: 432px;
    overflow: hidden;
    background: var(--paper);
  }
  .card--front { top: 105px; }
  .card--back { top: 589px; }
  .card__bg { position: absolute; inset: 0; width: 100%; height: 100%; }

  /* front */
  .brand-front {
    position: absolute; left: 190px; top: 100px; width: 210px;
    text-align: center; color: var(--white);
    font-weight: 700; font-size: 28px; letter-spacing: -0.5px;
  }
  .placeholder { position: absolute; border-radius: 6px; }
  .placeholder--customer { left: 76px; top: 93px; width: 56px; height: 72px; background: rgba(255,255,255,0.85); border-radius: 28px 28px 8px 8px; }
  .placeholder--shops { left: 420px; top: 88px; width: 156px; height: 75px; background: linear-gradient(180deg, #f3a88a 0%, #e9efee 35%, #cfe6e1 100%); }
  .pill {
    position: absolute; top: 183px; height: 17px; border-radius: 9px;
    background: var(--teal-soft); color: var(--white);
    font-size: 10px; font-weight: 600; line-height: 17px; text-align: center;
  }
  .pill--customer { left: 56px; width: 94px; }
  .pill--shops { left: 450px; width: 95px; }
  .url-band {
    position: absolute; display: flex; align-items: center; justify-content: center; gap: 7px;
    color: var(--white); font-weight: 700; font-size: 16px; letter-spacing: 0.6px;
  }
  .url-band--front { left: 192px; top: 229px; width: 232px; height: 23px; }
  .url-band svg { width: 16px; height: 16px; }
  .step { position: absolute; top: 280px; width: 130px; text-align: center; }
  .step__art { width: 100px; height: 100px; margin: 0 auto; position: relative; }
  .step__art svg { position: absolute; inset: 0; }
  .step__fill { position: absolute; left: 18px; top: 22px; width: 64px; height: 52px; border-radius: 5px; }
  .step__label { margin-top: 10px; font-size: 10.5px; line-height: 15px; text-transform: uppercase; }
  .step--1 { left: 21px; } .step--2 { left: 164px; } .step--3 { left: 316px; } .step--4 { left: 470px; }

  /* back */
  .brand-back {
    position: absolute; left: 24px; top: 40px;
    color: var(--teal-deep); font-weight: 700; font-size: 28px; letter-spacing: -0.5px;
  }
  .headline {
    position: absolute; left: 24px; top: 123px;
    font-family: "Bebas Neue", Impact, sans-serif; font-size: 37px; line-height: 35px; color: var(--ink);
  }
  .subline { position: absolute; left: 24px; top: 207px; font-size: 13.5px; font-weight: 600; }
  .tag {
    position: absolute; left: 23px; top: 241px; width: 186px; height: 19px;
    color: var(--white); font-size: 12px; font-weight: 600; letter-spacing: 1px; line-height: 19px; padding-left: 14px;
  }
  .tag svg { position: absolute; inset: 0; z-index: -1; }
  .checklist { position: absolute; left: 26px; top: 271px; list-style: none; }
  .checklist li { display: flex; align-items: center; gap: 12px; height: 27px; color: var(--white); font-size: 14.5px; }
  .tick { width: 17px; height: 17px; border-radius: 2px; background: var(--coral); display: flex; align-items: center; justify-content: center; }
  .claim { position: absolute; left: 24px; top: 357px; color: var(--white); font-style: italic; font-weight: 600; font-size: 13.5px; letter-spacing: -0.2px; }
  .url-band--back { left: 16px; top: 393px; width: 232px; height: 24px; justify-content: flex-start; padding-left: 28px; }
</style>
</head>
<body>

<section class="card card--front" aria-label="Flyer front">
  <svg class="card__bg" viewBox="0 0 610 432" preserveAspectRatio="none" aria-hidden="true">
    <rect width="610" height="432" fill="var(--paper-grey)"/>
    <path d="M0 0H610V218C420 290 190 290 0 220Z" fill="var(--teal)"/>
    <path d="M0 220C190 290 420 290 610 218V230C420 300 190 300 0 232Z" fill="var(--white)"/>
  </svg>
  <div class="placeholder" style="left:0;top:0;width:190px;height:215px;background:linear-gradient(180deg,rgba(255,255,255,0.05),rgba(255,255,255,0.12));border-radius:0" role="img" aria-label="Faint city skyline"></div>
  <div class="placeholder placeholder--customer" role="img" aria-label="Customer silhouette"></div>
  <div class="pill pill--customer">CUSTOMER</div>
  <div class="brand-front">ParcelLantern</div>
  <div class="placeholder placeholder--shops" role="img" aria-label="Three shop screens with striped awnings"></div>
  <div class="pill pill--shops">ONLINE SHOPS</div>
  <div class="url-band url-band--front">
    <svg viewBox="0 0 232 23" preserveAspectRatio="none" style="position:absolute;inset:0;width:100%;height:100%;z-index:-1" aria-hidden="true"><path d="M6 0H232L226 23H0Z" fill="var(--coral)"/></svg>
    <svg viewBox="0 0 16 16" aria-hidden="true"><rect x="4" y="2" width="8" height="12" rx="4" fill="none" stroke="#fff" stroke-width="1.6"/><line x1="8" y1="2" x2="8" y2="7" stroke="#fff" stroke-width="1.6"/></svg>
    <span>parcellantern.com</span>
  </div>

  <div class="step step--1">
    <div class="step__art">
      <svg viewBox="0 0 100 100" aria-hidden="true"><path d="M10 60A42 42 0 1 1 90 60" fill="none" stroke="var(--teal-ring)" stroke-width="2"/></svg>
      <div class="step__fill" style="left:34px;width:34px;height:66px;background:linear-gradient(180deg,#f3f3f3,#2f8fd0)" role="img" aria-label="Phone with payment receipt"></div>
    </div>
    <p class="step__label">Request &amp;<br>Payment</p>
  </div>
  <div class="step step--2">
    <div class="step__art">
      <svg viewBox="0 0 100 100" aria-hidden="true"><path d="M10 60A42 42 0 1 1 90 60" fill="none" stroke="var(--teal-ring)" stroke-width="2"/></svg>
      <div class="step__fill" style="left:8px;width:86px;background:linear-gradient(180deg,#f3a88a 0%,#2fa592 30%,#2fa592 80%,#dcdcdc 100%)" role="img" aria-label="Shop screen with awning"></div>
    </div>
    <p class="step__label">Order &amp;<br>Purchase</p>
  </div>
  <div class="step step--3">
    <div class="step__art">
      <svg viewBox="0 0 100 100" aria-hidden="true"><path d="M10 60A42 42 0 1 1 90 60" fill="none" stroke="var(--teal-ring)" stroke-width="2"/></svg>
      <div class="step__fill" style="left:2px;width:92px;background:linear-gradient(90deg,#3cb3a0,#f2a98a,#ec7a4e)" role="img" aria-label="Shopping bags and parcels"></div>
    </div>
    <p class="step__label">Receive &amp;<br>Consolidate</p>
  </div>
  <div class="step step--4">
    <div class="step__art">
      <svg viewBox="0 0 100 100" aria-hidden="true"><path d="M10 60A42 42 0 1 1 90 60" fill="none" stroke="var(--teal-ring)" stroke-width="2"/></svg>
      <div class="step__fill" style="left:-6px;width:98px;background:linear-gradient(90deg,#e4664a 0%,#e4664a 30%,#d9b27a 30%,#d9b27a 100%)" role="img" aria-label="Delivery truck carrying boxes"></div>
    </div>
    <p class="step__label">Shipping<br>Worldwide</p>
  </div>
</section>

<section class="card card--back" aria-label="Flyer back">
  <svg class="card__bg" viewBox="0 0 606 433" preserveAspectRatio="none" aria-hidden="true">
    <rect width="610" height="433" fill="var(--paper)"/>
    <path d="M0 150C40 120 120 90 170 0H470C380 80 220 150 0 200Z" fill="var(--white)" opacity="0.7"/>
    <path d="M0 150C150 255 420 265 610 132V433H0Z" fill="var(--teal-soft)"/>
    <path d="M0 150C40 190 90 215 150 232C90 240 40 240 0 236Z" fill="#8fd3c8" opacity="0.5"/>
  </svg>
  <div class="brand-back">ParcelLantern</div>
  <h1 class="headline">Now you can shop for<br>Korean products.</h1>
  <p class="subline">FROM ANYWHERE, WITHOUT HEADACHE</p>
  <div class="tag">
    <svg viewBox="0 0 186 19" preserveAspectRatio="none" aria-hidden="true"><path d="M4 0H186L180 19H0Z" fill="var(--coral)"/></svg>
    HOW IT WORKS
  </div>
  <ul class="checklist">
    <li><span class="tick"><svg width="12" height="10" viewBox="0 0 12 10" aria-hidden="true"><path d="M1 5L4.5 8.5L11 1.5" fill="none" stroke="#fff" stroke-width="2.2"/></svg></span>FIND WHAT YOU WANT WITH A HELPING HAND</li>
    <li><span class="tick"><svg width="12" height="10" viewBox="0 0 12 10" aria-hidden="true"><path d="M1 5L4.5 8.5L11 1.5" fill="none" stroke="#fff" stroke-width="2.2"/></svg></span>LET ME KNOW WHAT YOU NEED</li>
    <li><span class="tick"><svg width="12" height="10" viewBox="0 0 12 10" aria-hidden="true"><path d="M1 5L4.5 8.5L11 1.5" fill="none" stroke="#fff" stroke-width="2.2"/></svg></span>CALM YOUR BEATING HEART UNTIL THE DELIVERY</li>
  </ul>
  <p class="claim">I NOT ONLY MAKE IT EASY, IT’S SMART TO SHOP WITH PARCELLANTERN.</p>
  <div class="url-band url-band--back">
    <svg viewBox="0 0 232 24" preserveAspectRatio="none" style="position:absolute;inset:0;width:100%;height:100%;z-index:-1" aria-hidden="true"><path d="M6 0H232L226 24H0Z" fill="var(--teal-deep)"/></svg>
    <svg viewBox="0 0 16 16" aria-hidden="true"><rect x="4" y="2" width="8" height="12" rx="4" fill="none" stroke="#fff" stroke-width="1.6"/><line x1="8" y1="2" x2="8" y2="7" stroke="#fff" stroke-width="1.6"/></svg>
    <span>parcellantern.com</span>
  </div>
</section>

</body>
</html>
```